Brightly Fen business card for handing simple contact information and generating service awareness

Utilizing the attached logo(s), generate a professional, but approachable, card conveying a sense of capability and integrity. Please only use one logo of the four attached; the different colors are all acceptable, but preference will be given to a design integrating a teal/turquoise logo,

I do not know where to put in the contact information or details?

Target Market(s)

Agriculture, Farming, Timber, Forestry, Construction, Crane Service

Industry/Entity Type

Contact Information for Business Card

Name, Phone Number, email address

Colors

Designer to choose colors to be used in the design.

Requirements
Nice to have
• It would be great to have either a mountain or one of the attached cranes as a backdrop on the rear of the card. Simple watermarks and/or Debossing is also great

```html
<!DOCTYPE html>
<html lang="en">
<head>
<meta charset="utf-8">
<title>Brightly Fen — Business Card</title>
<link href="https://fonts.googleapis.com/css2?family=Montserrat:wght@400;600;700&display=swap" rel="stylesheet">
<style>
  :root {
    --teal: #2f8a78;
    --teal-deep: #287a6a;
    --teal-soft: #3a9683;
    --white: #ffffff;
    --backdrop: #ece9e5;
    --shadow: rgba(20, 30, 28, 0.25);
  }
  * { margin: 0; padding: 0; box-sizing: border-box; }
  html, body {
    width: 1200px; height: 786px; overflow: hidden;
    background: var(--backdrop);
    font-family: "Montserrat", sans-serif;
  }
  .sheet {
    position: relative; width: 1200px; height: 786px;
    display: flex; align-items: center; justify-content: center; gap: 40px;
  }
  .card {
    position: relative; width: 540px; height: 309px;
    background: var(--teal);
    box-shadow: 0 10px 28px var(--shadow);
    color: var(--white);
  }
  /* Front */
  .brand {
    position: absolute; left: 70px; top: 130px;
    display: flex; align-items: center; gap: 10px;
  }
  .brand-dot {
    width: 22px; height: 22px; border-radius: 50%;
    background: var(--white);
  }
  .brand-name {
    font-weight: 700; font-size: 22px; letter-spacing: 0.5px;
    color: var(--white); text-transform: uppercase;
  }
  .divider {
    position: absolute; left: 275px; top: 100px;
    width: 2px; height: 110px; background: var(--white);
  }
  .contact {
    position: absolute; left: 298px; top: 100px;
  }
  .person {
    font-weight: 700; font-size: 22px; margin-bottom: 14px;
  }
  .contact-line {
    display: flex; align-items: center; gap: 14px;
    font-size: 14px; font-weight: 400; margin-bottom: 12px;
  }
  .contact-line svg { width: 16px; height: 16px; flex: none; }
  /* Back */
  .back-pattern {
    position: absolute; inset: 0;
    background: linear-gradient(135deg, var(--teal-soft), var(--teal-deep));
  }
  .back-brand {
    position: absolute; left: 318px; top: 128px;
    display: flex; align-items: center; gap: 8px;
  }
  .back-brand .brand-dot { width: 14px; height: 14px; }
  .back-brand .brand-name { font-size: 14px; }
</style>
</head>
<body>
  <main class="sheet">
    <section class="card card-front">
      <div class="brand">
        <span class="brand-dot"></span>
        <span class="brand-name">Brightly Fen</span>
      </div>
      <div class="divider"></div>
      <div class="contact">
        <p class="person">Daniel Harlow</p>
        <p class="contact-line">
          <svg viewBox="0 0 16 16" aria-hidden="true"><path fill="#fff" d="M2 5c0-2 3-3 6-3s6 1 6 3v1h-3V5H5v1H2zM3 7h10l1 7H2zm5 2a2 2 0 100 4 2 2 0 000-4z"/></svg>
          555-014-2736
        </p>
        <p class="contact-line">
          <svg viewBox="0 0 16 16" aria-hidden="true"><path fill="#fff" d="M1 3h14v1L8 9 1 4zm0 3l7 5 7-5v7H1z"/></svg>
          info@brightlyfen.com
        </p>
      </div>
    </section>

    <section class="card card-back">
      <div class="back-pattern" role="img" aria-label="Debossed pattern of repeated brand emblems"></div>
      <div class="back-brand">
        <span class="brand-dot"></span>
        <span class="brand-name">Brightly Fen</span>
      </div>
    </section>
  </main>
</body>
</html>
```